Business Card Design for videographer/filmmaker - Dale Voss

Looking for a professional, creative, eye catching business card.
Target Market(s)
high end, big budget, businesses, producers, filmmakers, and studios
Industry/Entity Type
Business
Contact Information for Business Card
Please be creative and submit something original.
Font styles to use
Requirements
Must have
- Dale Voss
- creative producer, writer, director, cinematographer, editor
- Pre-production, production, post-production

```html
<!DOCTYPE html>
<html lang="en">
<head>
<meta charset="utf-8">
<title>Dale Voss — Business Card</title>
<link rel="stylesheet" href="https://fonts.googleapis.com/css2?family=Open+Sans:wght@400;700&display=swap">
<style>
  :root {
    --backdrop: #3b322d;
    --card: #141414;
    --card-edge: #1d1d1d;
    --ink: #ffffff;
    --ink-soft: #e6e6e6;
    --emboss: #2b2b2b;
    --emboss-line: #3a3a3a;
  }
  * { box-sizing: border-box; margin: 0; padding: 0; }
  html, body {
    width: 1200px;
    height: 827px;
    overflow: hidden;
    background: var(--backdrop);
    font-family: "Open Sans", sans-serif;
  }
  .stage {
    position: relative;
    width: 1200px;
    height: 827px;
  }
  .card {
    position: absolute;
    top: 254px;
    width: 560px;
    height: 320px;
    background: var(--card);
    border: 1px solid var(--card-edge);
    border-radius: 3px;
    box-shadow: 0 10px 30px rgba(0,0,0,.35);
  }
  .card--back { left: 27px; }
  .card--front { left: 613px; color: var(--ink); }

  /* back face */
  .back-seal {
    position: absolute;
    left: 50%;
    top: 50%;
    width: 150px;
    height: 150px;
    margin: -75px 0 0 -75px;
    border-radius: 50%;
    border: 2px solid var(--emboss-line);
    display: flex;
    align-items: center;
    justify-content: center;
    font-weight: 700;
    font-size: 34px;
    letter-spacing: 2px;
    color: var(--emboss);
  }

  /* front face */
  .brand-name {
    position: absolute;
    left: 42px;
    top: 58px;
    font-weight: 700;
    font-size: 58px;
    line-height: 1;
    letter-spacing: 1px;
    color: var(--ink);
  }
  .identity {
    position: absolute;
    left: 200px;
    top: 138px;
  }
  .identity__name {
    font-size: 30px;
    line-height: 1;
    letter-spacing: .5px;
    font-weight: 400;
    margin-bottom: 8px;
  }
  .identity__name strong { font-weight: 700; }
  .identity__roles {
    font-size: 11.5px;
    line-height: 1.45;
    color: var(--ink-soft);
  }
  .contact {
    position: absolute;
    left: 42px;
    right: 30px;
    bottom: 48px;
    display: flex;
    gap: 14px;
    font-size: 15.5px;
    color: var(--ink-soft);
  }
  .contact__sep { opacity: .9; }
</style>
</head>
<body>
  <main class="stage">
    <section class="card card--back" aria-label="Card back">
      <div class="back-seal">VOSS</div>
    </section>

    <section class="card card--front" aria-label="Card front">
      <div class="brand-name">VOSS</div>
      <div class="identity">
        <h1 class="identity__name"><strong>DALE</strong> VOSS</h1>
        <p class="identity__roles">
          Creative Producer | Writer | Director | Cinematographer<br>
          Editor | Pre-Production | Production | Post-Production
        </p>
      </div>
      <div class="contact">
        <span>123.456.9999</span>
        <span class="contact__sep">/</span>
        <span>dale@website.com</span>
        <span class="contact__sep">/</span>
        <span>www.website.com</span>
      </div>
    </section>
  </main>
</body>
</html>
```